Welcome signage for KJT Software Consulting Company

I need Welcome signage for KJT Consulting company Office Window. We are a Computer software company that offers software Implementation and Training for our Customers windows size 1. 900mm high 750mm wide. size 2. 1000mm high 700 wide.
Please review our website for branding and ideas.
The poster needs to contain our logo, website www.kjtconsulting-example.net.au and ph number 1300 46 81 07 , and the strap line... Empowering businesses with software choice.
Updates

Hi I'm really keen to find the perfect design. I had decided on one however the designer was dismissed from the group by admin so here I go again. Please read the briefs already in the information and hopefully I am excited by new submissions when I arrive to work on Monday xxx Thanks heaps fellow Designers x

```html
<!DOCTYPE html>
<html lang="en">
<head>
<meta charset="utf-8">
<title>KJT Consulting – Window Signage</title>
<link rel="stylesheet" href="https://fonts.googleapis.com/css2?family=Rubik:wght@500;700&family=Poppins:wght@400;500&display=swap">
<style>
  :root {
    --canvas: #ffffff;
    --frame: #9a9a9a;
    --panel: #262729;
    --brand-grey: #dcdcdc;
    --yellow: #fdd10a;
    --white: #ffffff;
    --ink: #1f1f1f;
  }
  * { box-sizing: border-box; margin: 0; padding: 0; }
  html, body { width: 1200px; height: 561px; overflow: hidden; background: var(--canvas); }
  .board {
    position: relative; width: 1200px; height: 561px;
    border: 1px solid var(--frame); background: var(--canvas);
  }
  .sign {
    position: absolute; background: var(--panel); overflow: hidden;
    font-family: "Rubik", sans-serif;
  }
  .sign--small { left: 58px; top: 100px; width: 487px; height: 406px; }
  .sign--large { left: 576px; top: 47px; width: 555px; height: 463px; }

  .brand {
    position: absolute; left: 0; right: 0; text-align: center;
    color: var(--brand-grey); font-weight: 500; letter-spacing: 0.06em; line-height: 1;
  }
  .sign--small .brand { top: 52px; font-size: 76px; }
  .sign--large .brand { top: 70px; font-size: 84px; }

  .strapline {
    position: absolute; left: 0; right: 0; text-align: center;
    color: var(--white); font-weight: 700; text-transform: uppercase; line-height: 1.24;
  }
  .strapline em { font-style: normal; color: var(--yellow); }
  .sign--small .strapline { top: 186px; font-size: 26px; letter-spacing: 0.12em; }
  .sign--large .strapline { top: 211px; font-size: 30px; letter-spacing: 0.12em; }

  .services {
    position: absolute; background: var(--yellow); list-style: none;
    display: flex; justify-content: space-around; align-items: center;
    font-family: "Poppins", sans-serif; color: var(--ink); text-align: center;
  }
  .sign--small .services { left: 63px; top: 277px; width: 341px; height: 64px; padding: 0 8px; font-size: 7px; line-height: 1.3; }
  .sign--large .services { left: 49px; top: 309px; width: 461px; height: 87px; padding: 0 12px; font-size: 10px; line-height: 1.3; }
  .service { display: flex; flex-direction: column; align-items: center; }
  .service svg { fill: none; stroke: var(--ink); stroke-width: 1.6; stroke-linecap: round; stroke-linejoin: round; }
  .sign--small .service svg { width: 22px; height: 22px; margin-bottom: 5px; }
  .sign--large .service svg { width: 30px; height: 30px; margin-bottom: 7px; }

  .contact-band { position: absolute; left: 0; width: 100%; }
  .sign--small .contact-band { top: 365px; height: 26px; }
  .sign--large .contact-band { top: 416px; height: 30px; }
  .contact-band svg { position: absolute; inset: 0; width: 100%; height: 100%; }
  .contact-band .white { fill: var(--white); }
  .contact-band .yellow { fill: var(--yellow); }
  .web, .phone {
    position: absolute; top: 0; height: 100%; display: flex; align-items: center;
    color: var(--ink); font-weight: 500;
  }
  .phone { font-weight: 700; }
  .sign--small .web { left: 28px; font-size: 12px; letter-spacing: 0.03em; }
  .sign--small .phone { left: 300px; font-size: 11px; letter-spacing: 0.05em; }
  .sign--large .web { left: 30px; font-size: 14px; letter-spacing: 0.03em; }
  .sign--large .phone { left: 359px; font-size: 13px; letter-spacing: 0.05em; }
</style>
</head>
<body>
<svg width="0" height="0" style="position:absolute" aria-hidden="true">
  <defs>
    <symbol id="icon-review" viewBox="0 0 32 32">
      <path d="M8 22h-1a5 5 0 0 1 0-10 7 7 0 0 1 13-2 5 5 0 0 1 6 5"/>
      <circle cx="20" cy="20" r="5"/><path d="M24 24l5 5"/>
    </symbol>
    <symbol id="icon-config" viewBox="0 0 32 32">
      <circle cx="12" cy="12" r="4"/>
      <path d="M12 3v3M12 18v3M3 12h3M18 12h3M5.6 5.6l2 2M16.4 16.4l2 2M5.6 18.4l2-2M16.4 7.6l2-2"/>
      <path d="M17 21l8-8 3 1-1-3-2 2M17 21l-3 3a1.5 1.5 0 0 0 2 2l3-3z"/>
    </symbol>
    <symbol id="icon-migration" viewBox="0 0 32 32">
      <rect x="4" y="5" width="14" height="20"/><rect x="7" y="8" width="14" height="20"/>
      <path d="M10 13h8M10 17h8M10 21h8M21 17h9M27 14l3 3-3 3"/>
    </symbol>
    <symbol id="icon-integration" viewBox="0 0 32 32">
      <rect x="4" y="12" width="14" height="16"/><path d="M11 12v16M4 20h14"/>
      <path d="M15 4h12v12H15z"/><path d="M19 8h4"/>
    </symbol>
    <symbol id="icon-training" viewBox="0 0 32 32">
      <circle cx="10" cy="18" r="3"/><circle cx="22" cy="18" r="3"/>
      <path d="M4 29a6 6 0 0 1 12 0M16 29a6 6 0 0 1 12 0"/>
      <path d="M9 11l7-5 7 5M20 6l6-3"/>
    </symbol>
  </defs>
</svg>

<main class="board">
  <section class="sign sign--small" aria-label="Window sign, 900 by 750 mm">
    <p class="brand">KJT</p>
    <h1 class="strapline">Empowering <em>businesses</em><br>with <em>software</em> choice</h1>
    <ul class="services">
      <li class="service"><svg><use href="#icon-review"/></svg>Software<br>Review</li>
      <li class="service"><svg><use href="#icon-config"/></svg>Software<br>Configuration</li>
      <li class="service"><svg><use href="#icon-migration"/></svg>Software<br>Migration</li>
      <li class="service"><svg><use href="#icon-integration"/></svg>Software<br>Integration</li>
      <li class="service"><svg><use href="#icon-training"/></svg>Software<br>Training</li>
    </ul>
    <div class="contact-band">
      <svg viewBox="0 0 487 26" preserveAspectRatio="none" aria-hidden="true">
        <polygon class="white" points="0,0 260,0 242,26 0,26"/>
        <polygon class="yellow" points="266,0 487,0 487,26 248,26"/>
      </svg>
      <span class="web">www.kjtconsulting-example.net.au</span>
      <span class="phone">Ph : 1300 46 81 07</span>
    </div>
  </section>

  <section class="sign sign--large" aria-label="Window sign, 1000 by 700 mm">
    <p class="brand">KJT</p>
    <h1 class="strapline">Empowering <em>businesses</em><br>with <em>software</em> choice</h1>
    <ul class="services">
      <li class="service"><svg><use href="#icon-review"/></svg>Software<br>Review</li>
      <li class="service"><svg><use href="#icon-config"/></svg>Software<br>Configuration</li>
      <li class="service"><svg><use href="#icon-migration"/></svg>Software<br>Migration</li>
      <li class="service"><svg><use href="#icon-integration"/></svg>Software<br>Integration</li>
      <li class="service"><svg><use href="#icon-training"/></svg>Software<br>Training</li>
    </ul>
    <div class="contact-band">
      <svg viewBox="0 0 555 30" preserveAspectRatio="none" aria-hidden="true">
        <polygon class="white" points="0,0 297,0 277,30 0,30"/>
        <polygon class="yellow" points="303,0 555,0 555,30 284,30"/>
      </svg>
      <span class="web">www.kjtconsulting-example.net.au</span>
      <span class="phone">Ph: 1300 46 81 07</span>
    </div>
  </section>
</main>
</body>
</html>
```